Business card for a plastic surgeon

i need a business card for a plastic surgeon. I have two adresses. The card should communicate safety, simmetry, beauty and with soft colors.
What i want in the card:
- my logo: Letters "R"and "B" (picture uploaded)
- my name: Renato Bastiani
- my registration: CRM 507 219
- my adresses and phone numbers (2):
- Av Dr Teixeira Lopes, 2710, sala 305 - Vila Olímpia | São Paulo/ SP - Phone: 11 4172-5036
- Al. Itapeva, 47, 3 andar - Alphaville | Barueri/ SP - Phone: 11 6350-2481

- my social network: site, facebook and instagram

Target Market(s)

people (95% girls and women) that want cosmetic procedures and plastic surgery

Industry/Entity Type

Business

Contact Information for Business Card

The card should communicate safety, simmetry, beauty and with soft colors.
Beige, brown, gray, rosy are some options. Color is free

Font styles to use
Serif

Requirements
Must have
• - my logo: Letters "R"and "B" (picture uploaded)
• - my name: Renato Bastiani
• - my registration: CRM 507 219
• - my adresses and phone numbers (2):
• - Av Dr Teixeira Lopes, 2710, sala 305 - Vila Olímpia | São Paulo/ SP - Phone: 11 4172-5036
• - Al. Itapeva, 47, 3 andar - Alphaville | Barueri/ SP - Phone: 11 6350-2481
• - my social network: site, facebook and instagram
Should not have
• other images (only my logo)

```html
<!DOCTYPE html>
<html lang="pt-BR">
<head>
<meta charset="utf-8">
<title>Dr. Renato Bastiani — Cartão de visita</title>
<link rel="stylesheet" href="https://fonts.googleapis.com/css2?family=Cinzel:wght@400&family=Cormorant+Garamond:wght@400;500&display=swap">
<style>
  :root {
    --backdrop: #eceded;
    --navy: #2e344f;
    --paper: #ffffff;
    --gold: #a8916c;
    --gold-soft: #c2ae8c;
    --ink: #8d7a5c;
    --shadow: rgba(40, 44, 60, 0.18);
  }
  * { box-sizing: border-box; margin: 0; padding: 0; }
  html, body {
    width: 1200px; height: 800px; overflow: hidden;
    background: var(--backdrop);
  }
  .sheet {
    width: 1200px; height: 800px;
    display: flex; align-items: center; justify-content: center; gap: 60px;
  }
  .card {
    width: 525px; height: 300px;
    position: relative;
    box-shadow: 0 10px 30px var(--shadow);
  }
  /* Front */
  .card--front { background: var(--navy); }
  .card--front .frame {
    position: absolute; inset: 14px;
    border: 1px solid var(--gold);
  }
  .identity {
    position: absolute; inset: 0;
    display: flex; flex-direction: column; align-items: center; justify-content: center;
    text-align: center;
  }
  .identity__mark {
    width: 10px; height: 10px; border-radius: 50%;
    background: var(--gold); margin-bottom: 18px;
  }
  .identity__name {
    font-family: "Cinzel", serif;
    font-size: 24px; letter-spacing: 1.5px;
    color: var(--gold);
  }
  .identity__role {
    font-family: "Cinzel", serif;
    font-size: 11px; letter-spacing: 4px;
    color: var(--gold); margin-top: 6px;
  }
  /* Back */
  .card--back { background: var(--paper); }
  .card--back .identity {
    right: 50%; bottom: 60px;
  }
  .card--back .identity__name { font-size: 18px; color: var(--ink); }
  .card--back .identity__role { font-size: 9px; letter-spacing: 3px; color: var(--ink); }
  .card--back .identity__mark { background: var(--ink); width: 8px; height: 8px; margin-bottom: 14px; }
  .divider {
    position: absolute; left: 50%; top: 60px; bottom: 80px;
    width: 1px; background: var(--gold-soft);
  }
  .contacts {
    position: absolute; left: calc(50% + 26px); top: 48px; right: 20px;
    font-family: "Cormorant Garamond", serif;
    font-size: 13.5px; line-height: 1.3; color: var(--ink);
  }
  .contacts__office { margin-bottom: 14px; }
  .line { display: flex; align-items: flex-start; gap: 7px; }
  .line svg { flex: none; margin-top: 3px; }
  .line--indent { padding-left: 17px; }
  .crm { padding-left: 17px; font-size: 12px; letter-spacing: 0.5px; }
  .social {
    position: absolute; left: 26px; right: 26px; bottom: 24px;
    display: flex; justify-content: space-between;
    font-family: "Cormorant Garamond", serif;
    font-size: 10.5px; letter-spacing: 0.8px; color: var(--ink);
  }
  .social__item { display: flex; align-items: center; gap: 6px; }
  .social__dot { width: 8px; height: 8px; border-radius: 50%; background: var(--ink); }
  .social__sq { width: 8px; height: 8px; background: var(--ink); }
</style>
</head>
<body>
<main class="sheet">
  <section class="card card--front" aria-label="Frente do cartão">
    <div class="frame"></div>
    <div class="identity">
      <span class="identity__mark"></span>
      <div class="identity__name">DR. RENATO BASTIANI</div>
      <div class="identity__role">CIRURGIÃO PLÁSTICO</div>
    </div>
  </section>

  <section class="card card--back" aria-label="Verso do cartão">
    <div class="identity">
      <span class="identity__mark"></span>
      <div class="identity__name">DR. RENATO BASTIANI</div>
      <div class="identity__role">CIRURGIÃO PLÁSTICO</div>
    </div>
    <div class="divider"></div>

    <div class="contacts">
      <div class="contacts__office">
        <div class="line">
          <svg width="10" height="12" viewBox="0 0 10 12"><path d="M5 0.5a4 4 0 0 1 4 4c0 3-4 7-4 7s-4-4-4-7a4 4 0 0 1 4-4z" fill="none" stroke="currentColor"/><circle cx="5" cy="4.5" r="1.4" fill="currentColor"/></svg>
          <span>Av Dr Teixeira Lopes, 2710, sala 305 - Vila Olímpia<br>São Paulo/SP</span>
        </div>
        <div class="line">
          <svg width="10" height="10" viewBox="0 0 10 10"><path d="M2 0.8l2 2-1 1.2a6 6 0 0 0 3 3l1.2-1 2 2-1.3 1.5C4.5 9.3 0.7 5.5 0.5 2.1z" fill="none" stroke="currentColor"/></svg>
          <span>11 4172-5036</span>
        </div>
      </div>
      <div class="contacts__office">
        <div class="line">
          <svg width="10" height="12" viewBox="0 0 10 12"><path d="M5 0.5a4 4 0 0 1 4 4c0 3-4 7-4 7s-4-4-4-7a4 4 0 0 1 4-4z" fill="none" stroke="currentColor"/><circle cx="5" cy="4.5" r="1.4" fill="currentColor"/></svg>
          <span>Al. Itapeva, 47, 3 andar<br>Alphaville<br>Barueri/SP</span>
        </div>
        <div class="line">
          <svg width="10" height="10" viewBox="0 0 10 10"><path d="M2 0.8l2 2-1 1.2a6 6 0 0 0 3 3l1.2-1 2 2-1.3 1.5C4.5 9.3 0.7 5.5 0.5 2.1z" fill="none" stroke="currentColor"/></svg>
          <span>11 6350-2481</span>
        </div>
        <div class="crm">CRM 507 219</div>
      </div>
    </div>

    <div class="social">
      <span class="social__item"><span class="social__sq"></span>DR.RENATOBASTIANI</span>
      <span class="social__item"><span class="social__dot"></span>@RENATO_BASTIANI_57</span>
      <span class="social__item"><span class="social__dot"></span>LUMENSA.COM.BR</span>
    </div>
  </section>
</main>
</body>
</html>
```